label design for oral care product

Kindly invite you to design bottle label (114 mm*40 mm) for our product, a kind of oral care product. The GEL is different from our previous cleanser product, as the pic we uploaded for demonstration. The color of frosted glass bottle is dark green, but the cap is white. You could download the pic of bottle among the uploaded files. The logo file and label content description are attached too. Please check them. Our product is made from many kinds of natural plant extracts, which includes herb and fruit. I wish the label would make our product look high-end and reliable. And it would be better if you could give some advice on paper material and special requirements for printing, related to your design. I value the texture of label too, because I think that stands for the quality of products. No color limitation for the use of our logo.
Target Market(s)
20-40 female, who value oral health.
Colors
Designer to choose colors to be used in the design.
Look and feel
Each slider illustrates characteristics of the customer's brand and the style your logo design should communicate.

```html
<!DOCTYPE html>
<html lang="en">
<head>
<meta charset="utf-8">
<title>Mintara Aligner Gel – Bottle Label</title>
<link rel="stylesheet" href="https://fonts.googleapis.com/css2?family=Roboto:ital,wght@0,400;0,500;0,700;0,900;1,900&display=swap">
<style>
  :root {
    --page-bg: #ffffff;
    --label-deep: #27296a;
    --label-mid: #2d3f8e;
    --label-bright: #2f56a8;
    --accent-red: #d9262b;
    --accent-red-dark: #b81d22;
    --text-light: #ffffff;
    --ring: rgba(255, 255, 255, 0.07);
  }
  * { box-sizing: border-box; margin: 0; padding: 0; }
  html, body {
    width: 1200px;
    height: 882px;
    overflow: hidden;
    background: var(--page-bg);
    font-family: "Roboto", Arial, sans-serif;
  }
  .canvas {
    position: relative;
    width: 1200px;
    height: 882px;
  }
  .label {
    position: absolute;
    left: 60px;
    top: 252px;
    width: 1080px;
    height: 378px;
    background: linear-gradient(90deg, var(--label-deep) 0%, var(--label-mid) 30%, var(--label-bright) 50%, var(--label-mid) 72%, var(--label-deep) 100%);
    color: var(--text-light);
    overflow: visible;
  }
  .label-rings {
    position: absolute;
    inset: 0;
    width: 100%;
    height: 100%;
    overflow: hidden;
  }
  .claim-tab {
    position: absolute;
    left: 334px;
    top: -6px;
    width: 402px;
    height: 50px;
    background: linear-gradient(180deg, var(--accent-red) 0%, var(--accent-red-dark) 100%);
    clip-path: polygon(0 0, 100% 0, 96% 100%, 4% 100%);
    display: flex;
    align-items: center;
    justify-content: center;
    font-size: 20px;
    font-weight: 500;
    letter-spacing: 0.2px;
  }
  .info-column {
    position: absolute;
    top: 62px;
    width: 300px;
  }
  .info-column.contents { left: 39px; }
  .info-column.directions { left: 725px; width: 305px; }
  .info-heading {
    font-size: 22px;
    font-weight: 700;
    padding-bottom: 10px;
    border-bottom: 3px solid var(--accent-red);
    width: 247px;
    margin-bottom: 12px;
  }
  .directions .info-heading { width: 290px; }
  .info-body {
    font-size: 21px;
    line-height: 28px;
  }
  .origin {
    margin-top: 28px;
    text-align: center;
    font-size: 21px;
  }
  .brand-block {
    position: absolute;
    left: 340px;
    top: 70px;
    width: 400px;
    text-align: center;
  }
  .brand-name {
    display: inline-flex;
    align-items: center;
    gap: 10px;
    font-size: 46px;
    font-weight: 900;
    line-height: 1;
    color: var(--text-light);
  }
  .brand-dot {
    width: 14px;
    height: 14px;
    border-radius: 50%;
    background: var(--text-light);
  }
  .product-name {
    display: inline-block;
    margin-top: 24px;
    width: 212px;
    height: 48px;
    background: var(--text-light);
    transform: skewX(-14deg);
    box-shadow: 6px 4px 0 rgba(0, 0, 0, 0.18);
  }
  .product-name span {
    display: block;
    transform: skewX(14deg);
    line-height: 48px;
    color: var(--accent-red);
    font-size: 27px;
    font-weight: 900;
    font-style: italic;
    letter-spacing: 0.5px;
  }
  .tagline {
    margin-top: 20px;
    font-size: 21px;
    line-height: 28px;
  }
  .volume {
    margin-top: 28px;
    font-size: 21px;
  }
</style>
</head>
<body>
<main class="canvas">
  <section class="label">
    <svg class="label-rings" viewBox="0 0 1080 378" aria-hidden="true">
      <circle cx="140" cy="120" r="150" fill="none" stroke="var(--ring)" stroke-width="26"/>
      <circle cx="975" cy="110" r="150" fill="none" stroke="var(--ring)" stroke-width="26"/>
      <circle cx="540" cy="189" r="230" fill="none" stroke="rgba(255,255,255,0.04)" stroke-width="20"/>
    </svg>

    <div class="claim-tab">Immune Support for Oral Health</div>

    <div class="info-column contents">
      <h2 class="info-heading">Contains:</h2>
      <p class="info-body">a proprietary blend of natural plant extract including Angelica, Radix Rehmanniae, Coptis, Honeysuckle, Echinacea, Sage, Chamomile, Acerola cherry.</p>
    </div>

    <div class="brand-block">
      <div class="brand-name"><span>Mintara</span><span class="brand-dot"></span></div>
      <div><div class="product-name"><span>ALIGNER GEL</span></div></div>
      <p class="tagline">the Solution to Maintain Dental<br>Hygiene and Strengthen Gums</p>
      <p class="volume">30 ml / 1 fl oz</p>
    </div>

    <div class="info-column directions">
      <h2 class="info-heading">Directions:</h2>
      <p class="info-body">Drop on the teeth directly after brushing. Or, put into clear aligners before wearing again. No need to rinse your mouth with water.</p>
      <p class="origin">Made in Taiwan</p>
    </div>
  </section>
</main>
</body>
</html>
```